business card for an electronic retail store

take our existing color logo, design a new business card and make a black&white version of the logo as well

Industry/Entity Type

Electronic

```html
<!DOCTYPE html>
<html lang="en">
<head>
<meta charset="UTF-8">
<title>Voltline Business Card</title>
<link rel="stylesheet" href="https://fonts.googleapis.com/css2?family=Exo+2:wght@400;500&family=Tinos&display=swap">
<style>
  :root {
    --backdrop: #3a3a3c;
    --card-black: #0d0d0d;
    --card-white: #ffffff;
    --brand-yellow: #ffd400;
    --accent-red: #d71f2b;
    --ink: #3a3a3a;
    --icon-grey: #6f6f73;
  }
  * { margin: 0; padding: 0; box-sizing: border-box; }
  html, body {
    width: 1200px; height: 816px; overflow: hidden;
    background: var(--backdrop);
  }
  .card {
    position: absolute; left: 100px; top: 122px;
    width: 1000px; height: 571px;
    border-radius: 36px; overflow: hidden;
    background: var(--card-black);
    font-family: "Exo 2", sans-serif;
    color: var(--ink);
  }
  .card-shapes { position: absolute; inset: 0; }
  .contact-person {
    position: absolute; left: 62px; top: 172px;
    display: flex; align-items: center; gap: 18px;
  }
  .person-name { font-size: 27px; font-weight: 500; letter-spacing: 1px; line-height: 1.05; }
  .person-role { font-size: 21px; letter-spacing: 1.5px; }
  .contact-list {
    position: absolute; left: 78px; top: 300px;
    list-style: none;
  }
  .contact-item {
    display: flex; align-items: center; gap: 22px;
    margin-bottom: 26px;
    font-size: 21px; line-height: 1.15; letter-spacing: 1px;
  }
  .contact-icon { width: 44px; height: 44px; flex: none; }
  .brand-block {
    position: absolute; left: 850px; top: 285px;
    transform: translate(-50%, -50%) rotate(90deg);
    white-space: nowrap; text-align: left;
  }
  .brand-name {
    display: flex; align-items: center; gap: 14px;
    font-size: 54px; font-weight: 500; letter-spacing: 3px;
    color: var(--card-white); line-height: 1;
  }
  .brand-mark { width: 26px; height: 26px; background: var(--accent-red); }
  .brand-tagline {
    font-family: "Tinos", serif;
    font-size: 24px; color: var(--card-white);
    margin-top: 12px; letter-spacing: 0.5px;
  }
</style>
</head>
<body>
  <div class="card">
    <svg class="card-shapes" width="1000" height="571" viewBox="0 0 1000 571">
      <polygon class="yellow-frame" fill="var(--brand-yellow)"
        points="0,0 600,0 618,22 650,22 712,110 712,461 612,571 0,571"/>
      <polygon class="white-panel" fill="var(--card-white)"
        points="0,0 560,0 660,120 660,452 580,571 0,571"/>
      <line class="name-rule" x1="0" y1="250" x2="520" y2="250" stroke="var(--accent-red)" stroke-width="4"/>
    </svg>

    <div class="contact-person">
      <svg class="contact-icon" viewBox="0 0 44 44">
        <circle cx="22" cy="22" r="22" fill="var(--icon-grey)"/>
        <circle cx="22" cy="17" r="7" fill="var(--card-white)"/>
        <path d="M10 33 q12 -14 24 0 z" fill="var(--card-white)"/>
      </svg>
      <div>
        <div class="person-name">MARCUS WHITFIELD</div>
        <div class="person-role">Managing Director</div>
      </div>
    </div>

    <ul class="contact-list">
      <li class="contact-item">
        <svg class="contact-icon" viewBox="0 0 44 44">
          <circle cx="22" cy="22" r="22" fill="var(--accent-red)"/>
          <rect x="16" y="11" width="12" height="22" rx="2" fill="none" stroke="#fff" stroke-width="2.2"/>
          <circle cx="22" cy="29" r="1.4" fill="#fff"/>
        </svg>
        <span>012 555 0147<br>012 555 0193</span>
      </li>
      <li class="contact-item">
        <svg class="contact-icon" viewBox="0 0 44 44">
          <circle cx="22" cy="22" r="22" fill="var(--accent-red)"/>
          <rect x="11" y="13" width="22" height="14" rx="1.5" fill="none" stroke="#fff" stroke-width="2.2"/>
          <line x1="22" y1="27" x2="22" y2="31" stroke="#fff" stroke-width="2.2"/>
          <line x1="16" y1="32" x2="28" y2="32" stroke="#fff" stroke-width="2.2"/>
        </svg>
        <span>hello@voltline.com<br>voltlineaudio.com</span>
      </li>
      <li class="contact-item">
        <svg class="contact-icon" viewBox="0 0 44 44">
          <circle cx="22" cy="22" r="22" fill="var(--accent-red)"/>
          <path d="M22 34 C15 25 14 22 14 19 a8 8 0 0 1 16 0 c0 3 -1 6 -8 15 z" fill="#fff"/>
          <circle cx="22" cy="19" r="3" fill="var(--accent-red)"/>
        </svg>
        <span>27, 4th floor,Plaza<br>Station Road KLG</span>
      </li>
    </ul>

    <div class="brand-block">
      <div class="brand-name"><span class="brand-mark"></span>VOLTLINE</div>
      <div class="brand-tagline">Car Audio • Performance • Security</div>
    </div>
  </div>
</body>
</html>
```